Flyer Design Dental Office Grand Opening offer

Dental office.

Grand opening flyer. Offer Exam + cleaning + xrays.
special: free teeth whitening ($200 value)

Target Market(s)

Middle class people around Huntington Beach.

Industry/Entity Type

Dental Clinic

Colors
cfeae6
86cfc6
fac994
fee18a
e667a6

Requirements
Must have
• Do not change my existing logo
Nice to have
• Have some appealing picture/design to catch the eye, but not too flashy
Should not have
• No cartoon kind of design

```html
<!DOCTYPE html>
<html lang="en">
<head>
<meta charset="utf-8">
<title>Daybreak Dental – Grand Opening Flyer</title>
<link rel="stylesheet" href="https://fonts.googleapis.com/css2?family=Open+Sans:wght@400;600;700;800&family=Anton&family=Oswald:wght@600&display=swap">
<style>
  :root {
    --page-bg: #f2f2f2;
    --teal: #1e8f9e;
    --teal-dark: #146b77;
    --orange: #ee5a1c;
    --ink: #1c1c1c;
    --white: #ffffff;
    --band: #0d0d0d;
    --card: #f4f4f4;
    --card-lower: #d3e3ee;
    --sand: #e9d3b8;
  }
  * { box-sizing: border-box; margin: 0; padding: 0; }
  html, body { width: 1200px; height: 1200px; overflow: hidden; background: var(--page-bg); }
  body { font-family: "Open Sans", sans-serif; color: var(--ink); }

  .flyer {
    position: absolute; left: 160px; top: 18px;
    width: 880px; height: 1164px; overflow: hidden;
    box-shadow: 0 18px 40px rgba(0,0,0,.25);
  }
  .photo {
    position: absolute; inset: 0;
    background:
      radial-gradient(ellipse 45% 38% at 35% 42%, #e7c9b4 0%, #d9b49c 45%, rgba(217,180,156,0) 75%),
      radial-gradient(ellipse 30% 25% at 20% 18%, #4a3b34 0%, rgba(74,59,52,0) 80%),
      linear-gradient(160deg, #f3f3f3 0%, #dedede 45%, #cdbfb2 80%, #e2cbb0 100%);
  }

  .brand {
    position: absolute; left: 40px; top: 48px;
    width: 420px; height: 120px;
    background: var(--white); border-radius: 14px;
    display: flex; align-items: center; gap: 20px; padding: 0 28px;
    box-shadow: 0 4px 12px rgba(0,0,0,.12);
  }
  .brand-square { width: 74px; height: 74px; background: var(--teal); flex: none; }
  .brand-name { font-weight: 700; font-size: 40px; color: var(--teal); line-height: 1; }

  .contact { position: absolute; right: 50px; top: 60px; text-align: left; }
  .contact-label { font-size: 19px; color: #333; }
  .contact-phone { display: flex; align-items: center; gap: 14px; margin-top: 6px; font-size: 36px; font-weight: 700; color: var(--ink); }
  .contact-phone svg { width: 38px; height: 38px; }

  .promo {
    position: absolute; right: 70px; top: 300px;
    width: 400px; background: var(--card);
    box-shadow: 0 6px 16px rgba(0,0,0,.2);
  }
  .promo-ribbon {
    position: relative; margin: 22px -30px 0; height: 50px;
    background: var(--teal); color: var(--white);
    font-weight: 700; font-size: 28px; letter-spacing: 3px;
    display: flex; align-items: center; justify-content: center;
  }
  .promo-exam { padding: 18px 26px 20px; }
  .exam-line { display: flex; align-items: baseline; gap: 6px; }
  .exam-price { font-family: "Oswald", sans-serif; font-weight: 600; font-size: 60px; color: var(--ink); }
  .exam-title { font-weight: 800; font-size: 62px; color: var(--orange); }
  .exam-note { font-size: 17px; color: #222; margin-top: -4px; }
  .promo-bleach { background: var(--card-lower); padding: 20px 22px 18px; }
  .bleach-row { display: flex; align-items: center; gap: 18px; }
  .bleach-photo { width: 110px; height: 110px; border-radius: 50%; flex: none;
    background: radial-gradient(circle, #f4f4f4 0%, #d8636a 55%, #e9c4b3 100%); }
  .bleach-free { font-weight: 800; font-size: 62px; color: var(--orange); line-height: 1; }
  .bleach-title { font-weight: 700; font-size: 32px; color: var(--ink); }
  .bleach-note { font-size: 15px; color: #333; margin-top: 8px; text-align: center; }

  .band {
    position: absolute; left: 0; right: 0; top: 830px; height: 250px;
    background: var(--band); color: var(--white); text-align: center;
    padding-top: 24px;
  }
  .band-insurance { display: flex; align-items: center; justify-content: center; gap: 20px; font-size: 38px; font-weight: 400; }
  .band-insurance::before, .band-insurance::after { content: ""; width: 90px; height: 3px; background: var(--teal); }
  .band-title { font-family: "Anton", sans-serif; font-size: 104px; line-height: 1.05; letter-spacing: 2px; color: #e9e9e9; }
  .band-details { display: flex; justify-content: center; align-items: center; gap: 16px; font-size: 26px; color: #e5e5e5; }
  .band-details .divider { width: 2px; height: 30px; background: var(--teal); }
  .band-details strong { font-weight: 700; color: var(--white); }

  .floor { position: absolute; left: 0; right: 0; top: 1080px; bottom: 0; background: var(--sand); }
</style>
</head>
<body>
  <main class="flyer">
    <div class="photo" role="img" aria-label="Smiling patient reclining in a dental chair while a dentist holds a mirror"></div>

    <div class="brand">
      <span class="brand-square"></span>
      <span class="brand-name">daybreak dental</span>
    </div>

    <div class="contact">
      <p class="contact-label">Contact us for more information</p>
      <p class="contact-phone">
        <svg viewBox="0 0 24 24" aria-hidden="true"><circle cx="12" cy="12" r="12" fill="#1c1c1c"/><path d="M8.6 6.5l1.6 2.4-1 1.3c.7 1.5 1.9 2.7 3.5 3.5l1.3-1 2.4 1.6-.6 2c-4.6-.3-8.2-3.9-8.6-8.6z" fill="#fff"/></svg>
        (555) 014-2270
      </p>
    </div>

    <section class="promo">
      <div class="promo-ribbon">PROMOTIONS</div>
      <div class="promo-exam">
        <div class="exam-line"><span class="exam-price">$50</span><span class="exam-title">Exam</span></div>
        <p class="exam-note">with X-rays &amp; Cleaning (Regular)</p>
      </div>
      <div class="promo-bleach">
        <div class="bleach-row">
          <div class="bleach-photo" role="img" aria-label="Close-up of a bright white smile"></div>
          <div>
            <div class="bleach-free">FREE</div>
            <div class="bleach-title">Bleaching</div>
          </div>
        </div>
        <p class="bleach-note">(after completion of dental treatment)</p>
      </div>
    </section>

    <section class="band">
      <p class="band-insurance">PPO, HMO, StateCare welcomed</p>
      <h1 class="band-title">Grand Opening</h1>
      <p class="band-details">
        <span>Saturday</span><span class="divider"></span>
        <strong>March 24</strong><span class="divider"></span>
        <span>2218, Harbor Ave, Seacliff Point</span>
      </p>
    </section>

    <div class="floor"></div>
  </main>
</body>
</html>
```